Ad for Cyber Security Company- Print Ad

We are looking for an awesome designer to create a one page advertisement for the Brigmore Security data analytics platform that will be featured in an upcoming security magazine. This is also going to be featured in an upcoming trade show. Brigmore Security produced the BRIGMORE platform to help companies unify their security environment and help them address Insider Threat, Fraud and Anomaly ID and resolution. BRIGMORE uses an an advanced ingestion engine, machine learning, and workflow automation to ensure the right people are getting the right info at the right time. We serve enterprise level customers, augmenting and enhancing, not replacing their existing security stack. We would like few or single image, clean, and open ad built around the tagline 'Make Security a Team Sport.' We would like the logo to be featured, and include our website address on the page (www.brigmoresecurity.example). See below for style guide.

Target Market(s)

Industry insiders, Chief Information Security Officers (CISO) and Technical directors.

Font styles to use
Other font styles liked:
• See style guide, but we are open to suggestion.

Requirements
Must have
• A single image (minimum), Feature the provided logo, Include the tagline 'Make Security a Team Sport' and have the website somewhere on the ad. The image should focus on the conveying the message of "Make Security a Team Sport" and not be a generic security (padlock, network, etc.) image.
• See included style guide.

```html
<!DOCTYPE html>
<html lang="en">
<head>
<meta charset="utf-8">
<title>Brigmore Security – Make Security a Team Sport</title>
<link rel="stylesheet" href="https://fonts.googleapis.com/css2?family=Roboto+Condensed:ital,wght@1,800&family=Ubuntu:wght@300;500;700&display=swap">
<style>
  :root {
    --orange: #f26322;
    --orange-deep: #d94e14;
    --charcoal: #2a2a2a;
    --charcoal-soft: #363636;
    --graphite: #444446;
    --paper: #ffffff;
    --paper-grey: #f1f1f1;
    --ink: #3a3a3c;
    --social-a: #3b5a9a;
    --social-b: #0a79b0;
  }
  html, body {
    margin: 0;
    padding: 0;
    width: 960px;
    height: 1200px;
    overflow: hidden;
    background: var(--paper);
  }
  .ad {
    position: relative;
    width: 960px;
    height: 1200px;
    overflow: hidden;
    font-family: "Ubuntu", sans-serif;
  }
  .ad__shapes {
    position: absolute;
    inset: 0;
  }
  .brand {
    position: absolute;
    left: 78px;
    top: 62px;
    display: flex;
    align-items: center;
    gap: 18px;
  }
  .brand__mark {
    width: 62px;
    height: 62px;
    background: var(--orange);
  }
  .brand__name {
    font-family: "Ubuntu", sans-serif;
    font-weight: 700;
    font-size: 38px;
    line-height: 36px;
    letter-spacing: 2px;
    color: var(--ink);
    text-transform: uppercase;
  }
  .tagline {
    position: absolute;
    left: 94px;
    top: 560px;
    margin: 0;
    font-family: "Roboto Condensed", sans-serif;
    font-style: italic;
    font-weight: 800;
    font-size: 72px;
    line-height: 79px;
    letter-spacing: -1px;
    color: var(--paper);
  }
  .features {
    position: absolute;
    top: 866px;
    left: 0;
    width: 960px;
    margin: 0;
    padding: 0;
    list-style: none;
  }
  .feature {
    position: absolute;
    top: 0;
    width: 260px;
    margin-left: -130px;
    text-align: center;
  }
  .feature--anomaly { left: 219px; }
  .feature--insider { left: 470px; }
  .feature--activity { left: 730px; }
  .feature__icon {
    display: block;
    width: 86px;
    height: 86px;
    margin: 0 auto;
  }
  .feature__label {
    display: block;
    margin-top: 24px;
    font-weight: 500;
    font-size: 22px;
    color: var(--paper);
  }
  .feature__label::after {
    content: "";
    display: block;
    width: 32px;
    height: 4px;
    margin: 12px auto 0;
    background: var(--orange);
  }
  .social {
    position: absolute;
    top: 1075px;
    left: 799px;
    display: flex;
    gap: 18px;
  }
  .social__dot {
    width: 34px;
    height: 34px;
    border-radius: 50%;
  }
  .social__dot--one { background: var(--social-a); }
  .social__dot--two { background: var(--social-b); }
  .website {
    position: absolute;
    right: 72px;
    top: 1130px;
    margin: 0;
    font-size: 29px;
    font-weight: 300;
    letter-spacing: 2px;
    color: var(--paper);
  }
  .website strong { font-weight: 700; }
</style>
</head>
<body>
<main class="ad">
  <svg class="ad__shapes" width="960" height="1200" viewBox="0 0 960 1200">
    <defs>
      <linearGradient id="header-fade" x1="0" y1="0" x2="1" y2="1">
        <stop offset="0" stop-color="#ffffff"/>
        <stop offset="1" stop-color="#ececec"/>
      </linearGradient>
      <linearGradient id="photo-tones" x1="0" y1="0" x2="1" y2="1">
        <stop offset="0" stop-color="#c9cfc6"/>
        <stop offset="0.45" stop-color="#9b7a62"/>
        <stop offset="0.8" stop-color="#7d5a44"/>
        <stop offset="1" stop-color="#a58a72"/>
      </linearGradient>
      <linearGradient id="base-dark" x1="0" y1="0" x2="1" y2="1">
        <stop offset="0" stop-color="#2e2e2e"/>
        <stop offset="0.5" stop-color="#262626"/>
        <stop offset="1" stop-color="#323232"/>
      </linearGradient>
    </defs>
    <rect class="header" width="960" height="260" fill="url(#header-fade)"/>
    <polygon class="header__band" points="520,184 960,107 960,163" fill="var(--graphite)"/>
    <polygon class="base" points="0,855 960,723 960,1200 0,1200" fill="url(#base-dark)"/>
    <g role="img" aria-label="Photo of a smiling team of colleagues gathered around a café table, sharing tablets and phones">
      <polygon class="photo" points="0,234 960,161 960,723 0,855" fill="url(#photo-tones)"/>
    </g>
    <polygon class="photo__overlay" points="0,449 672,660 672,762 0,855" fill="var(--orange-deep)" opacity="0.88"/>
    <polygon class="footer-band" points="323,1094 960,1016 960,1200 288,1200" fill="var(--orange)"/>
  </svg>

  <div class="brand" aria-label="Brigmore Security">
    <span class="brand__mark"></span>
    <span class="brand__name">Brigmore<br>Security</span>
  </div>

  <h1 class="tagline">Make<br>Security a<br>Team Sport</h1>

  <ul class="features">
    <li class="feature feature--anomaly">
      <svg class="feature__icon" viewBox="0 0 86 86" aria-hidden="true">
        <circle cx="43" cy="43" r="42" fill="var(--orange)" stroke="#fff" stroke-width="1.5"/>
        <g fill="none" stroke="#fff" stroke-width="2">
          <rect x="22" y="24" width="42" height="36" rx="2"/>
          <line x1="22" y1="31" x2="64" y2="31"/>
          <line x1="27" y1="38" x2="38" y2="38"/>
          <line x1="27" y1="44" x2="36" y2="44"/>
          <line x1="27" y1="50" x2="38" y2="50"/>
          <circle cx="49" cy="44" r="7"/>
          <line x1="54" y1="49" x2="62" y2="57"/>
        </g>
      </svg>
      <span class="feature__label">Anomaly Detection</span>
    </li>
    <li class="feature feature--insider">
      <svg class="feature__icon" viewBox="0 0 86 86" aria-hidden="true">
        <circle cx="43" cy="43" r="42" fill="var(--orange)" stroke="#fff" stroke-width="1.5"/>
        <g fill="none" stroke="#fff" stroke-width="2">
          <rect x="21" y="24" width="44" height="30" rx="2"/>
          <line x1="43" y1="54" x2="43" y2="61"/>
          <line x1="35" y1="62" x2="51" y2="62"/>
          <circle cx="40" cy="38" r="8"/>
          <line x1="46" y1="44" x2="58" y2="56"/>
        </g>
      </svg>
      <span class="feature__label">Insider Threat</span>
    </li>
    <li class="feature feature--activity">
      <svg class="feature__icon" viewBox="0 0 86 86" aria-hidden="true">
        <circle cx="43" cy="43" r="42" fill="var(--orange)" stroke="#fff" stroke-width="1.5"/>
        <g fill="none" stroke="#fff" stroke-width="2">
          <rect x="22" y="30" width="40" height="26" rx="2"/>
          <line x1="42" y1="56" x2="42" y2="62"/>
          <line x1="34" y1="62" x2="50" y2="62"/>
          <path d="M30 22 h18 l6 6 v16 h-24 z"/>
          <line x1="34" y1="30" x2="46" y2="30"/>
          <circle cx="50" cy="46" r="6"/>
          <line x1="54" y1="50" x2="60" y2="56"/>
        </g>
      </svg>
      <span class="feature__label">User Activity Reviews</span>
    </li>
  </ul>

  <div class="social" aria-hidden="true">
    <span class="social__dot social__dot--one"></span>
    <span class="social__dot social__dot--two"></span>
  </div>

  <p class="website">www.<strong>brigmoresecurity</strong>.example</p>
</main>
</body>
</html>
```